Medical Billing - Professional Marketing Flier

We are needing help designing a clean and professional looking easy to read marketing flier for a medical billing practice. The text needs to be large enough to print. We are looking for a 5.5 x 8.5 design that we can edit the text as needed. I have included our logo and what we initially want it to say. Please keep in mind, we also want our logo and contact details on the flier. Let me know if you have any questions.

```html
<!DOCTYPE html>
<html lang="en">
<head>
<meta charset="utf-8">
<title>Lyra Billing Partners – Flier</title>
<link rel="stylesheet" href="https://fonts.googleapis.com/css2?family=Bowlby+One&family=Montserrat:wght@400;500;600;700;800&family=Merriweather:wght@700&family=Poppins:wght@700;800&display=swap">
<style>
  :root {
    --blue: #3b6ab5;
    --ink: #1f1f21;
    --paper: #ffffff;
    --text: #222226;
    --dots: #8a8a8a;
  }
  * { margin: 0; padding: 0; box-sizing: border-box; }
  html, body { width: 791px; height: 1200px; overflow: hidden; background: var(--paper); }
  .flier { position: relative; width: 791px; height: 1200px; overflow: hidden; font-family: "Montserrat", sans-serif; color: var(--text); }
  .backdrop { position: absolute; inset: 0; }
  .abs { position: absolute; white-space: nowrap; }

  .headline { font-family: "Bowlby One", sans-serif; color: var(--blue); line-height: 1; letter-spacing: -0.5px; }
  .headline--one { left: 89px; top: 40px; font-size: 43.4px; }
  .headline--two { left: 103px; top: 84px; font-size: 50px; }
  .website { left: 107px; top: 142px; font-family: "Merriweather", serif; font-weight: 700; font-size: 18px; color: var(--ink); }

  .brand { left: 524px; top: 92px; display: flex; align-items: center; gap: 9px; }
  .brand__dot { width: 28px; height: 28px; border-radius: 50%; background: var(--blue); flex: none; }
  .brand__name { font-family: "Montserrat", sans-serif; font-weight: 600; font-size: 14px; color: var(--blue); letter-spacing: 0.3px; }

  .intro { left: 108px; top: 172px; font-size: 14.5px; line-height: 16.8px; color: var(--text); }

  .check { position: absolute; width: 32px; height: 32px; border-radius: 50%; background: var(--blue); }
  .check svg { position: absolute; left: 8px; top: 8px; }
  .point__title { font-weight: 600; font-size: 23.5px; color: var(--paper); line-height: 1; }
  .point__bar { position: absolute; width: 54px; height: 4px; background: var(--blue); }
  .point__text { font-size: 14.7px; line-height: 17.4px; color: #e9e9ec; font-weight: 400; }
  .dotline { position: absolute; border-top: 2px dotted var(--dots); height: 0; }
  .dotline--v { border-top: none; border-left: 2px dotted var(--dots); width: 0; }

  .about { left: 418px; top: 340px; width: 310px; text-align: center; font-weight: 600; font-size: 25.5px; color: var(--ink); line-height: 1; }
  .cred-title { left: 416px; top: 364px; font-weight: 600; font-size: 34.5px; color: var(--blue); line-height: 1; letter-spacing: 0.5px; }
  .cred-text { left: 419px; top: 409px; font-size: 13.5px; line-height: 17.3px; color: var(--text); }

  .feature { font-family: "Poppins", sans-serif; font-weight: 800; font-size: 12px; line-height: 11.5px; color: var(--blue); letter-spacing: -0.3px; }
  .feature--loose { line-height: 16px; }

  .call { position: absolute; left: 67px; top: 868px; width: 72px; height: 72px; border-radius: 50%; background: var(--blue); }
  .call svg { position: absolute; left: 18px; top: 18px; }

  .touch-title { left: 44px; top: 956px; font-family: "Poppins", sans-serif; font-weight: 800; font-size: 22.5px; color: var(--blue); letter-spacing: -1.2px; line-height: 1; }
  .touch-phone { left: 44px; top: 979px; font-family: "Poppins", sans-serif; font-weight: 800; font-size: 24px; color: var(--ink); letter-spacing: -1px; line-height: 1.1; }
  .pin { position: absolute; left: 219px; top: 976px; }
  .address { left: 254px; top: 976px; font-weight: 700; font-size: 11.5px; line-height: 14px; color: var(--ink); }
  .touch-text { left: 44px; top: 1020px; font-size: 14.8px; line-height: 17.4px; color: var(--text); }

  .services-kicker { left: 430px; top: 886px; font-family: "Poppins", sans-serif; font-weight: 800; font-size: 22px; color: var(--blue); letter-spacing: -1px; line-height: 1; }
  .services-title { left: 430px; top: 907px; font-family: "Poppins", sans-serif; font-weight: 800; font-size: 26.5px; color: var(--ink); letter-spacing: -1px; line-height: 1; }
  .services-list { left: 431px; top: 939px; list-style: none; font-size: 12.4px; line-height: 16.75px; letter-spacing: 3.2px; color: var(--ink); }
</style>
</head>
<body>
<main class="flier">
  <svg class="backdrop" width="791" height="1200" viewBox="0 0 791 1200" aria-hidden="true">
    <rect x="0" y="30" width="791" height="990" fill="var(--ink)"/>
    <path d="M0,0 L0,45 L108,305 C132,362 190,394 252,379 L791,238 L791,0 Z" fill="var(--blue)"/>
    <path d="M10,0 L120,300 C142,350 192,372 247,360 L791,236 L791,0 Z" fill="var(--paper)"/>
    <path d="M418,336 C376,370 362,422 376,472 L475,812 L663,752 L791,752 L791,300 Z" fill="var(--paper)"/>
    <path d="M139,918 L663,752 C720,736 772,762 791,800 L791,1020 L200,1020 Z" fill="var(--blue)"/>
    <path d="M0,953 L622,795 C682,780 722,800 742,850 L791,1018 L791,1200 L0,1200 Z" fill="var(--paper)"/>
  </svg>

  <div class="abs headline headline--one">YOUR PRACTICAL</div>
  <div class="abs headline headline--two">MEDICAL BILL</div>
  <div class="abs website">www.lyrabillingpartners.com</div>

  <div class="abs brand">
    <span class="brand__dot"></span>
    <span class="brand__name">LYRA BILLING PARTNERS</span>
  </div>

  <p class="abs intro">Would you prefer to spend time focusing on your clients and running your<br>practice rather than trying to stay up to speed with the constantly changing<br>medical billing rules and regulations? Let us help you by managing your<br>medical billing and dealing with the insurance companies on your behalf!<br>We work with you to tailor the entire medical billing process to suit your<br>practices needs while making it as smooth and painless as possible.</p>

  <span class="check" style="left:59px;top:431px"><svg width="16" height="16" viewBox="0 0 16 16"><path d="M2,7 L6.5,12.5 L14,2.5" fill="none" stroke="#fff" stroke-width="3" stroke-linecap="round" stroke-linejoin="round"/></svg></span>
  <div class="abs point__title" style="left:111px;top:431px">AGING</div>
  <span class="point__bar" style="left:113px;top:457px"></span>
  <p class="abs point__text" style="left:109px;top:471px">Are you leaving money on the<br>table? Are you able to do the<br>follow-through needed to keep<br>your aging in check and more<br>money flowing into your practice?</p>
  <span class="dotline" style="left:113px;top:567px;width:246px"></span>

  <span class="check" style="left:62px;top:593px"><svg width="16" height="16" viewBox="0 0 16 16"><path d="M2,7 L6.5,12.5 L14,2.5" fill="none" stroke="#fff" stroke-width="3" stroke-linecap="round" stroke-linejoin="round"/></svg></span>
  <div class="abs point__title" style="left:114px;top:593px">DECIDE WISE</div>
  <span class="point__bar" style="left:114px;top:619px"></span>
  <p class="abs point__text" style="left:113px;top:637px">Are you uncertain about how to get<br>insurance to pay on claims that should<br>be covered but for some reason they<br>decided not to?</p>
  <span class="dotline" style="left:113px;top:711px;width:246px"></span>

  <span class="check" style="left:60px;top:730px"><svg width="16" height="16" viewBox="0 0 16 16"><path d="M2,7 L6.5,12.5 L14,2.5" fill="none" stroke="#fff" stroke-width="3" stroke-linecap="round" stroke-linejoin="round"/></svg></span>
  <div class="abs point__title" style="left:118px;top:736px">CLEAN TRACKING</div>
  <span class="point__bar" style="left:118px;top:764px"></span>
  <p class="abs point__text" style="left:118px;top:781px">We can clean up your aging, reduce<br>the amount of time it takes for claims<br>to pay out, and we can keep your<br>aging to a minimum</p>

  <div class="abs about">ABOUT OUR</div>
  <div class="abs cred-title">CREDENTIALING</div>
  <p class="abs cred-text">Are you wanting to get contracted with<br>insurance companies but aren’t sure how<br>to go about it? Are you wanting to expand<br>your client base by having the option to bill<br>insurance? Let us take the confusion out of<br>what can seem like a daunting task! We<br>can get you and your practitioners<br>contracted with the insurance companies<br>of your choice and help you navigate<br>through the process every step of the way!</p>

  <span class="dotline dotline--v" style="left:573px;top:588px;height:184px"></span>
  <span class="dotline" style="left:453px;top:665px;width:248px"></span>
  <div class="abs feature" style="left:462px;top:622px">INFORMATION<br>SHARING</div>
  <div class="abs feature" style="left:592px;top:620px">CLAIMS PROCESSING<br>AND FOLLOW-UP</div>
  <div class="abs feature" style="left:485px;top:695px">PAYMENT<br>POSTING</div>
  <div class="abs feature feature--loose" style="left:595px;top:686px">CUSTOMER<br>SUPPORT</div>

  <span class="call"><svg width="36" height="36" viewBox="0 0 36 36"><path d="M12,4 C8,6 6,10 6,16 C6,24 10,30 15,33 L19,28 C19,27 18,26 16,25 C13,22 12,17 13,12 C15,11 16,10 16,9 L14,4 Z" fill="#fff"/></svg></span>

  <div class="abs touch-title">GET IN TOUCH</div>
  <div class="abs touch-phone">555-014-2273</div>
  <svg class="pin" width="20" height="26" viewBox="0 0 20 26" aria-hidden="true"><path d="M10,1.5 C5.3,1.5 1.5,5.2 1.5,9.8 C1.5,16 10,24.5 10,24.5 C10,24.5 18.5,16 18.5,9.8 C18.5,5.2 14.7,1.5 10,1.5 Z" fill="none" stroke="var(--blue)" stroke-width="1.8"/><circle cx="10" cy="9.8" r="3.6" fill="none" stroke="var(--blue)" stroke-width="1.8"/></svg>
  <div class="abs address">PO Box 418 Cedar Falls,<br>WA 98000</div>
  <p class="abs touch-text">If any of these processes are something you<br>would like our help with or to consult with us<br>on, please email us or give us a call! We<br>specialize in billing and contracting for<br>Nutritionists and Dietitians. We would love to<br>help you expand your business and take the<br>pain and frustration out of billing so you can<br>focus on your clients.</p>

  <span class="dotline dotline--v" style="left:402px;top:966px;height:182px"></span>

  <div class="abs services-kicker">OUR</div>
  <div class="abs services-title">SERVICES</div>
  <ul class="abs services-list">
    <li>Medical-legal Billing</li>
    <li>Posting and Claim Processing</li>
    <li>Billing all Insurance Companies</li>
    <li>Claim Follow-up and Resubmission</li>
    <li>Remittance and payment posting</li>
    <li>Reconciliation of EOPs</li>
    <li>Patient Statement and Processing</li>
    <li>Insurance Appeal</li>
    <li>Patient payment arrangement</li>
    <li>Insurance credentialing</li>
    <li>Billing audits</li>
    <li>Accounts Receivable (AR) Collections</li>
    <li>IT Support</li>
  </ul>
</main>
</body>
</html>
```